Folder Design (inside and out) for a medical technology company

We are a Medical Technology company looking for a professional folder design.
Folder design is for Front, Back, and the flaps inside the folder. We've provided a variety of products at a national level for 20 years, we're targeting a demographic of doctors and are looking to improve out materials.

I attached our logo for reference, please feel free to reach out if you have any questions. Please use the pink and blue logo.

Thank you.

Target Market(s)

Doctors

Industry/Entity Type

Medical, Technology

Requirements
Must have
• Professional design

```html
<!DOCTYPE html>
<html lang="en">
<head>
<meta charset="utf-8">
<title>Meridian Care – Presentation Folder</title>
<link href="https://fonts.googleapis.com/css2?family=Montserrat:wght@400;500;700&family=Ubuntu:wght@400;700&display=swap" rel="stylesheet">
<style>
  :root {
    --stage: #2f2f31;
    --blue: #6a8fcb;
    --blue-deep: #2f4f8f;
    --pink: #ee5a8a;
    --paper: #efefef;
    --paper-soft: #f7f7f7;
    --white: #ffffff;
    --safe: #1aa34a;
    --cut: #e0464f;
  }
  * { margin: 0; padding: 0; box-sizing: border-box; }
  html, body { width: 1200px; height: 2346px; overflow: hidden; background: var(--stage); }
  .canvas { position: relative; width: 1200px; height: 2346px; font-family: "Montserrat", sans-serif; }
  .dieline { position: absolute; inset: 0; }
  .abs { position: absolute; }
  .brand { text-align: center; font-family: "Ubuntu", sans-serif; }
  .brand-name { font-weight: 700; font-size: 50px; line-height: 1; }
  .brand-tag { font-family: "Ubuntu", sans-serif; font-weight: 400; font-size: 16px; margin-top: 8px; }
  .brand--white .brand-name, .brand--white .brand-tag { color: var(--white); }
  .brand--color .brand-name, .brand--color .brand-tag { color: var(--blue); }
  .pill { border-radius: 14px; color: var(--white); text-align: center; font-weight: 500; }
  .pill--web { width: 284px; height: 34px; line-height: 36px; font-size: 15px; border-radius: 12px 12px 0 0; }
  .pill--pink { background: var(--pink); }
  .pill--blue { background: var(--blue); }
  .contact-title { left: 212px; top: 469px; width: 232px; height: 33px; line-height: 34px; font-size: 21px; font-weight: 700; border-radius: 17px; }
  .contact-icons { left: 282px; top: 512px; width: 92px; display: flex; justify-content: space-between; }
  .contact-icons svg { width: 24px; height: 24px; }
  .contact-lines { left: 128px; top: 541px; width: 400px; text-align: center; color: var(--white); font-size: 17px; line-height: 21px; }
  .photo-frame { left: 675px; top: 253px; width: 390px; height: 390px; border-radius: 50%;
    background: radial-gradient(circle at 40% 35%, #e9c9b0 0%, #c8b39a 30%, #8fa96a 62%, #5f7f3f 100%); }
  .headline { left: 645px; top: 718px; width: 470px; text-align: center; color: var(--pink); font-weight: 700; font-size: 27px; line-height: 33px; }
  .pocket-offer { left: 712px; top: 908px; width: 366px; transform: rotate(180deg); }
  .pocket-offer p { color: var(--white); font-size: 12.5px; line-height: 17px; text-align: center; margin-bottom: 7px; }
  .pocket-offer .pill { width: 344px; margin-left: 11px; height: 31px; line-height: 32px; font-size: 15px; font-weight: 700; border-radius: 16px; margin-top: 6px; }
</style>
</head>
<body>
<div class="canvas">
  <svg class="dieline" width="1200" height="2346" viewBox="0 0 1200 2346" aria-hidden="true">
    <defs>
      <linearGradient id="innerPaper" x1="0" y1="0" x2="0" y2="1">
        <stop offset="0" stop-color="#f8f8f8"/>
        <stop offset="1" stop-color="#ececec"/>
      </linearGradient>
    </defs>

    <g class="sheet-outside">
      <rect x="55" y="41" width="548" height="820" fill="var(--blue)"/>
      <rect x="603" y="41" width="549" height="820" fill="var(--paper)"/>
      <path d="M55,861 H1152 V1139 H680 Q640,1139 635,1100 L606,880 Q602,868 598,880 L569,1100 Q564,1139 524,1139 H55 Z" fill="var(--blue)"/>
      <circle cx="875" cy="428" r="238" fill="none" stroke="var(--blue)" stroke-width="26"/>
      <circle cx="875" cy="428" r="213" fill="none" stroke="var(--pink)" stroke-width="18"/>
      <g stroke="var(--blue-deep)" stroke-width="3">
        <line x1="200" y1="958" x2="248" y2="911"/>
        <line x1="428" y1="911" x2="476" y2="958"/>
        <line x1="200" y1="1027" x2="248" y2="1073"/>
        <line x1="428" y1="1073" x2="476" y2="1027"/>
      </g>
      <path d="M55,41 H1152 V1139 H680 Q640,1139 635,1100 L606,880 Q602,868 598,880 L569,1100 Q564,1139 524,1139 H55 Z" fill="none" stroke="var(--cut)" stroke-width="4"/>
      <path d="M62,48 H1145 V1132 H682 Q646,1132 641,1098 L606,870 L563,1098 Q558,1132 522,1132 H62 Z" fill="none" stroke="var(--blue-deep)" stroke-width="3"/>
      <path d="M73,60 H1134 V1120 H686 Q654,1120 650,1092 L614,875 H590 L554,1092 Q550,1120 518,1120 H73 Z" fill="none" stroke="var(--safe)" stroke-width="3" stroke-dasharray="7 5"/>
      <line x1="55" y1="861" x2="1152" y2="861" stroke="var(--cut)" stroke-width="3" stroke-dasharray="8 4"/>
      <line x1="603" y1="41" x2="603" y2="861" stroke="var(--cut)" stroke-width="2" stroke-dasharray="8 4"/>
    </g>

    <g class="sheet-inside">
      <rect x="55" y="1184" width="1097" height="820" fill="url(#innerPaper)"/>
      <path d="M55,2004 H1152 V2282 H680 Q640,2282 635,2243 L606,2023 Q602,2011 598,2023 L569,2243 Q564,2282 524,2282 H55 Z" fill="var(--paper-soft)"/>
      <path d="M55,1184 H1152 V2282 H680 Q640,2282 635,2243 L606,2023 Q602,2011 598,2023 L569,2243 Q564,2282 524,2282 H55 Z" fill="none" stroke="var(--cut)" stroke-width="4"/>
      <path d="M62,1191 H1145 V2275 H682 Q646,2275 641,2241 L606,2013 L563,2241 Q558,2275 522,2275 H62 Z" fill="none" stroke="var(--blue-deep)" stroke-width="3"/>
      <path d="M73,1203 H1134 V2263 H686 Q654,2263 650,2235 L614,2018 H590 L554,2235 Q550,2263 518,2263 H73 Z" fill="none" stroke="var(--safe)" stroke-width="3" stroke-dasharray="7 5"/>
      <line x1="55" y1="2004" x2="603" y2="2004" stroke="var(--pink)" stroke-width="4"/>
      <line x1="603" y1="2004" x2="1152" y2="2004" stroke="var(--blue)" stroke-width="4"/>
      <line x1="55" y1="2008" x2="1152" y2="2008" stroke="var(--cut)" stroke-width="2" stroke-dasharray="8 4"/>
      <line x1="603" y1="1184" x2="603" y2="2004" stroke="var(--cut)" stroke-width="2" stroke-dasharray="8 4"/>
    </g>
  </svg>

  <!-- Back cover -->
  <div class="abs brand brand--white" style="left:128px; top:340px; width:400px;">
    <div class="brand-name">Meridian Care</div>
    <div class="brand-tag">Supplies delivered with steady care</div>
  </div>
  <div class="abs pill pill--pink contact-title">CONTACT DETAILS</div>
  <div class="abs contact-icons">
    <svg viewBox="0 0 24 24"><circle cx="12" cy="12" r="11" fill="var(--white)"/><path d="M12 5a4.5 4.5 0 0 0-4.5 4.5C7.5 13 12 18 12 18s4.5-5 4.5-8.5A4.5 4.5 0 0 0 12 5z" fill="var(--blue)"/><circle cx="12" cy="9.5" r="1.7" fill="var(--white)"/></svg>
    <svg viewBox="0 0 24 24"><circle cx="12" cy="12" r="11" fill="var(--white)"/><path d="M8 6.5l2 .3 1 3-1.4 1.2a8 8 0 0 0 3.4 3.4l1.2-1.4 3 1 .3 2c-.3 1-1.5 1.7-2.5 1.5A10 10 0 0 1 6.5 9c-.2-1 .5-2.2 1.5-2.5z" fill="var(--blue)"/></svg>
    <svg viewBox="0 0 24 24"><circle cx="12" cy="12" r="11" fill="var(--white)"/><rect x="6" y="8" width="12" height="8.5" rx="1" fill="var(--blue)"/><path d="M6.5 8.5 12 13l5.5-4.5" fill="none" stroke="var(--white)" stroke-width="1.3"/></svg>
  </div>
  <div class="abs contact-lines">
    Meridian Care<br>
    420 Harbor View Rd Ste 12<br>
    Lakeside, FL 33000<br>
    800.555.0142<br>
    info@meridiancaresupply.com
  </div>
  <div class="abs pill pill--web pill--pink" style="left:184px; top:827px;">www.meridiancaresupply.com</div>

  <!-- Front cover -->
  <div class="abs brand brand--color" style="left:675px; top:98px; width:400px;">
    <div class="brand-name">Meridian Care</div>
    <div class="brand-tag">Supplies delivered with steady care</div>
  </div>
  <div class="abs photo-frame" role="img" aria-label="Photo of a smiling senior couple embracing outdoors in a park"></div>
  <div class="abs headline">THE MOST CONVENIENT WAY<br>TO GET YOUR DIABETIC<br>SUPPLIES</div>
  <div class="abs pill pill--web pill--blue" style="left:735px; top:827px;">www.meridiancaresupply.com</div>

  <!-- Right pocket -->
  <div class="abs pocket-offer">
    <p>NO OUT OF POCKET COST: Click on a product below<br>to learn more and see if your health plan or insurance<br>will cover your diabetic supplies</p>
    <div class="pill pill--pink">CONTINUOUS GLUCOSE MONITOR</div>
    <div class="pill pill--pink">DIABETIC SHOES</div>
    <div class="pill pill--pink">VERIFY 1ST CGM SHIPMENT</div>
  </div>

  <!-- Inside panels -->
  <div class="abs brand brand--color" style="left:128px; top:1522px; width:400px;">
    <div class="brand-name">Meridian Care</div>
    <div class="brand-tag">Supplies delivered with steady care</div>
  </div>
  <div class="abs brand brand--color" style="left:675px; top:1522px; width:400px;">
    <div class="brand-name">Meridian Care</div>
    <div class="brand-tag">Supplies delivered with steady care</div>
  </div>
  <div class="abs pill pill--web pill--pink" style="left:184px; top:1970px;">www.meridiancaresupply.com</div>
  <div class="abs pill pill--web pill--blue" style="left:735px; top:1970px;">www.meridiancaresupply.com</div>
</div>
</body>
</html>
```